Mother's Day Sale Banner Ad For Jewelry Site

We are looking for a designer to design a banner on our website advertising our Mother's Day Sale. I have enclosed a few pieces of jewelry we would like used in the ad. The ad size needs to be 1187 × 400. The ad should say:

Mother's Day Sale - Save 15% with Promo Code: LOVEMOM

```html
<!DOCTYPE html>
<html lang="en">
<head>
<meta charset="utf-8">
<title>Mother's Day Sale Banner</title>
<link href="https://fonts.googleapis.com/css2?family=Montserrat:wght@300;400;800&display=swap" rel="stylesheet">
<style>
  :root {
    --bg-deep: #4a2116;
    --bg-mid: #6e3322;
    --bg-warm: #84412a;
    --band: #050505;
    --text: #ffffff;
    --gold-light: #e6c877;
    --gold-mid: #c9a047;
    --gold-dark: #8c6a26;
  }
  html, body {
    margin: 0;
    padding: 0;
    width: 1200px;
    height: 404px;
    overflow: hidden;
    background: var(--bg-deep);
  }
  .banner {
    position: relative;
    width: 1200px;
    height: 404px;
    overflow: hidden;
    font-family: "Montserrat", "Helvetica Neue", Arial, sans-serif;
  }
  .banner__backdrop {
    position: absolute;
    inset: 0;
    background:
      radial-gradient(ellipse at 45% 45%, var(--bg-warm) 0%, var(--bg-mid) 45%, var(--bg-deep) 100%);
  }
  .banner__jewelry {
    position: absolute;
    left: 92px;
    top: 82px;
    width: 380px;
    height: 252px;
    border-radius: 90px 120px 110px 80px;
    background:
      radial-gradient(ellipse at 30% 40%, var(--gold-light) 0%, var(--gold-mid) 45%, var(--gold-dark) 100%);
  }
  .banner__band {
    position: absolute;
    left: 493px;
    top: 162px;
    right: 0;
    height: 111px;
    background: var(--band);
  }
  .banner__headline {
    position: absolute;
    left: 521px;
    top: 176px;
    margin: 0;
    color: var(--text);
    font-weight: 300;
    font-size: 36.5px;
    line-height: 44px;
    letter-spacing: 0.2px;
    text-transform: uppercase;
    white-space: nowrap;
  }
  .banner__headline strong {
    font-weight: 800;
  }
</style>
</head>
<body>
  <main class="banner">
    <div class="banner__backdrop" role="img" aria-label="Rich brown background with a copper damask floral pattern"></div>
    <div class="banner__jewelry" role="img" aria-label="Pair of gold rope-twist earrings crossed with diamond-set white gold X bands"></div>
    <div class="banner__band"></div>
    <h1 class="banner__headline">Mother's Day Sale - Save 15%<br>With <strong>Promo Code: LOVEMOM</strong></h1>
  </main>
</body>
</html>
```